Postcard to accompany Open House invitation

We need a postcard to accompany on invitation to our school open house. The invitation will include the details of the event, the postcard should include general information about our school: address, phone number, picture(s). Our school is 6-12th grade and features 1-to-1 instruction as our primary method of instruction. Our key marketing messages are: individual student attention, customized instructional approach, and maximized academic achievement. The design should match our school logo and support the key message that students and teachers work together 1-to-1. Postcard will be included subsequently with admissions packets.
...I have uploaded some photos from our school showing good/typical interaction between student/teacher. You can use these for the design or pick others like them.
- This was included in the brief, but just to be clear: we do not want any Open House information on this postcard. A formal invitation to the Open House is being sent along with this postcard. The postcard should just include pictures and marketing copy.

```html
<!DOCTYPE html>
<html lang="en">
<head>
<meta charset="utf-8">
<title>The Larkwood School — One-to-One Learning, Grades 6–12</title>
<link href="https://fonts.googleapis.com/css2?family=Questrial&family=Pinyon+Script&family=Arimo:wght@700&display=swap" rel="stylesheet">
<style>
  :root {
    --paper: #e6e1d5;
    --ghost: #d9d4c9;
    --gold: #ad8d2c;
    --band-gold: #a88a34;
    --ink-grey: #7b7770;
    --ink-soft: #8d8983;
    --rule-dots: #b9b4aa;
    --link-blue: #1d3d8f;
    --school-navy: #1f3566;
  }
  * { margin: 0; padding: 0; box-sizing: border-box; }
  html, body { width: 927px; height: 1200px; overflow: hidden; background: var(--paper); }
  .postcard {
    position: relative;
    width: 927px;
    height: 1200px;
    background: var(--paper);
    font-family: "Questrial", "Century Gothic", sans-serif;
    color: var(--ink-grey);
    overflow: hidden;
  }
  .ghost-mark {
    position: absolute;
    top: -38px;
    left: 0;
    width: 927px;
    text-align: center;
    font-size: 260px;
    letter-spacing: 6px;
    line-height: 1;
    color: var(--ghost);
    white-space: nowrap;
  }
  .intro-line {
    position: absolute;
    top: 43px;
    width: 927px;
    text-align: center;
    font-size: 22px;
    color: var(--ink-soft);
    letter-spacing: 0.3px;
  }
  .headline {
    position: absolute;
    top: 100px;
    width: 927px;
    text-align: center;
    font-family: "Pinyon Script", cursive;
    font-weight: 400;
    font-size: 84px;
    line-height: 1;
    color: var(--gold);
  }
  .gold-band {
    position: absolute;
    left: 0;
    width: 927px;
    height: 10px;
    background: var(--band-gold);
  }
  .gold-band.top { top: 221px; }
  .gold-band.bottom { top: 690px; }
  .photo-area {
    position: absolute;
    top: 231px;
    left: 0;
    width: 927px;
    height: 459px;
    background:
      radial-gradient(ellipse at 30% 35%, #f1eee9 0%, rgba(241,238,233,0) 55%),
      linear-gradient(180deg, #e4dfd8 0%, #cfc8bf 48%, #3b3533 62%, #2b2727 100%);
  }
  .key-messages {
    position: absolute;
    top: 740px;
    width: 927px;
    text-align: center;
    font-size: 25px;
    line-height: 48.5px;
    color: var(--ink-grey);
    list-style: none;
  }
  .dotted-rule {
    position: absolute;
    top: 917px;
    left: 59px;
    width: 814px;
    border-top: 2px dotted var(--rule-dots);
  }
  .tour-note {
    position: absolute;
    top: 963px;
    left: 62px;
    font-size: 20px;
    line-height: 36px;
    color: var(--ink-grey);
  }
  .office-phone {
    position: absolute;
    top: 972px;
    left: 535px;
    font-family: "Arimo", Arial, sans-serif;
    font-weight: 700;
    font-size: 47px;
    letter-spacing: -0.5px;
    color: var(--gold);
  }
  .school-name {
    position: absolute;
    top: 1106px;
    left: 50px;
    display: flex;
    align-items: center;
    gap: 10px;
  }
  .school-name .mark {
    width: 56px;
    height: 56px;
    border-radius: 50%;
    background: var(--school-navy);
  }
  .school-name .name {
    font-size: 26px;
    color: var(--school-navy);
  }
  .contact {
    position: absolute;
    top: 1104px;
    right: 54px;
    text-align: right;
    font-size: 20px;
    line-height: 30px;
    color: var(--ink-grey);
  }
  .contact .web { color: var(--link-blue); }
</style>
</head>
<body>
  <main class="postcard">
    <div class="ghost-mark" aria-hidden="true">1-to-1</div>
    <p class="intro-line">The Larkwood School · Grades 6–12 · One-to-One Instruction</p>
    <h1 class="headline">Learning Together</h1>

    <div class="gold-band top"></div>
    <div class="photo-area" role="img" aria-label="Photograph of a teacher pointing to a textbook while working one-to-one with a student at a desk"></div>
    <div class="gold-band bottom"></div>

    <ul class="key-messages">
      <li>Individual student attention</li>
      <li>Customized instructional approach</li>
      <li>Maximized academic achievement</li>
    </ul>

    <div class="dotted-rule"></div>

    <p class="tour-note">To learn more about our school or to schedule<br>a private tour, please call our office</p>
    <p class="office-phone">(555) 014-2290</p>

    <div class="school-name">
      <span class="mark" aria-hidden="true"></span>
      <span class="name">The Larkwood School</span>
    </div>

    <p class="contact">4280 North Brayfield, Houston, Texas 77063<br><span class="web">www.larkwoodschool.com</span></p>
  </main>
</body>
</html>
```